Healthy diet charts design

4 pages separate not like a single flyer. I want to create a health education resources for my company Meadowbrook Health Care.
I am attaching some files for ideas and content but we need to create a unique I like design some charts food charts and
1. right eating habits
2. principles of eating
3. Food pyramid
4. green, yellow and red foods
with the creative design but our branding meadowbrook health care
and
MEADOWBROOK Acronym
Health principles
R - Right Nutrition
E - Exercise
S - Sunlight
T - Temperance
O - Optimal water intake
R - Rest
A - Air
T - Trust in divine power
I - Initiating social support
O - Optimism
N - New beginning
It still do not match my expectation.
usa
health care

```html
<!DOCTYPE html>
<html lang="en">
<head>
<meta charset="utf-8">
<title>Meadowbrook Health Care – Healthy Diet Charts</title>
<link rel="stylesheet" href="https://fonts.googleapis.com/css2?family=Poppins:wght@400;500;600;700;800&display=swap">
<style>
:root{
  --bg:#e8e8e8;
  --navy:#2d3558;
  --navy-dark:#262d4c;
  --green:#1f9a3e;
  --green-bright:#6cb33f;
  --green-light:#5cb84a;
  --yellow:#f7d417;
  --orange:#f58220;
  --orange-light:#f4ae3e;
  --tan:#c98a52;
  --red:#d91f26;
  --text:#2a2f45;
  --muted:#5a5e6e;
  --row-green:#c8e2c3;
  --row-yellow:#fff0a8;
  --row-red:#f4b9a3;
  --col-gray:#dedee2;
}
*{box-sizing:border-box;margin:0;padding:0}
html,body{width:919px;height:1200px;overflow:hidden}
body{background:var(--bg);font-family:"Poppins",sans-serif;color:var(--text);position:relative}
.page{position:absolute;width:424px;height:548px;background:#fff;overflow:hidden}
.page--eating{left:25px;top:26px}
.page--pyramid{left:470px;top:26px}
.page--codes{left:25px;top:608px}
.page--restore{left:470px;top:608px}
.page__header{position:absolute;left:0;top:0;width:100%;height:96px;
  background:linear-gradient(100deg,var(--navy-dark) 0%,var(--navy) 55%,#3b4a44 100%);
  color:#fff;text-align:center;display:flex;flex-direction:column;justify-content:center}
.page__title{font-weight:700;font-size:24px;line-height:1.05}
.page__kicker{font-weight:400;font-size:15px;line-height:1.1}
.page__strip{position:absolute;left:0;bottom:0;width:100%;height:8px;background:var(--green-bright)}
.brand{position:absolute;right:19px;bottom:16px;width:82px;text-align:center;
  font-weight:700;font-size:9px;line-height:1.15;color:var(--navy);letter-spacing:.3px}

/* acronym fan */
.acronym{position:absolute;left:5px;top:526px;width:0;height:0}
.acronym__arc{position:absolute;left:-40px;top:-40px}
.acronym__item{position:absolute;left:0;top:-4px;height:8px;line-height:8px;transform-origin:0 50%;white-space:nowrap;
  font-size:4.6px;font-weight:500;color:var(--muted);letter-spacing:.2px}
.acronym__letter{display:inline-block;width:7px;text-align:center;font-size:6.4px;font-weight:700;color:var(--navy);margin-right:1px}

/* page 1 */
.wheel{position:absolute;left:82px;top:146px}
.tip{position:absolute;font-size:6.6px;line-height:1.2;color:var(--text)}
.tip b{font-size:10px;font-weight:700;color:var(--navy)}
.tip--right{text-align:right}
.tip--center{text-align:center}
.quote{position:absolute;left:0;width:100%;top:450px;text-align:center;font-weight:600;font-size:9.6px;line-height:1.25;color:var(--navy)}

/* page 2 */
.intro{position:absolute;left:40px;width:344px;top:120px;text-align:center;font-size:7.6px;line-height:1.25;color:var(--text)}
.pyramid{position:absolute;left:0;top:0}
.level-label{position:absolute;font-size:6.8px;line-height:10px;color:var(--text);text-align:right;white-space:nowrap}
.side-note{position:absolute;font-size:6.6px;line-height:1.35;color:var(--muted)}
.side-note b{color:var(--navy);font-weight:600}

/* page 3 */
.dots{position:absolute;left:22px;top:77px;display:flex;gap:3px}
.dots span{width:8px;height:8px;border-radius:50%}
.photo-band{position:absolute;left:0;top:96px;width:100%;height:103px;
  background:linear-gradient(90deg,#cfcbc8 0%,#bdb7b4 35%,#8a6a4a 55%,#c5483a 70%,#5f8e3a 85%,#d8d4d1 100%)}
.table{position:absolute;left:0;top:0;width:100%;height:100%}
.col{position:absolute;top:223px;width:64px;height:236px;background:var(--col-gray);border-radius:20px 20px 6px 6px}
.col__icon{position:absolute;left:50%;top:4px;width:30px;height:30px;margin-left:-15px;border-radius:50%;background:#fff;border:2px solid #c4c5cb}
.col__head{position:absolute;left:-1px;right:-1px;top:40px;height:18px;background:var(--navy);color:#fff;
  font-weight:700;font-size:8.6px;line-height:18px;text-align:center}
.col__arrow{position:absolute;left:50%;top:63px;margin-left:-6px;width:0;height:0;border-left:6px solid transparent;border-right:6px solid transparent;border-top:7px solid var(--navy)}
.cell{position:absolute;width:64px;height:45px;display:flex;align-items:center;justify-content:center;text-align:center;font-size:6.6px;line-height:1.2;color:#4a4d59;padding:0 3px}
.row-key{position:absolute;left:21px;width:60px;height:43px;border-radius:22px 0 0 22px}
.row-key__dot{position:absolute;left:3px;top:3px;width:37px;height:37px;border-radius:50%;border:3px solid #fff;display:flex;align-items:center;justify-content:center}

/* page 4 */
.card{position:absolute;top:107px;width:121px}
.card__tab{display:block}
.card__photo{height:49px}
.card__title{height:35px;color:#fff;text-align:center;font-size:11px;line-height:1.15;padding-top:3px}
.card__title b{font-weight:700;display:block}
.card__lead{height:28px;display:flex;align-items:center;justify-content:center;text-align:center;font-style:italic;font-size:6.3px;line-height:1.2;padding:0 6px;color:var(--text)}
.card__list{list-style:none;padding:4px 5px 4px 13px;font-size:6.2px;line-height:1.22;color:var(--text)}
.card__list li{position:relative;margin-bottom:1px}
.card__list li::before{content:"";position:absolute;left:-7px;top:3px;width:2.5px;height:2.5px;border-radius:50%;background:var(--text)}
.card__list b{font-weight:600}
.card--green{left:20px}
.card--yellow{left:151px}
.card--red{left:283px}
.card--green .card__title{background:var(--green)}
.card--green .card__lead{background:#b9dcb3}
.card--green .card__list{background:linear-gradient(#e6f2e3,#fff 90%)}
.card--yellow .card__title{background:var(--yellow)}
.card--yellow .card__lead{background:#fbe99a}
.card--yellow .card__list{background:linear-gradient(#fdf6d2,#fff 90%)}
.card--red .card__title{background:var(--red)}
.card--red .card__lead{background:#f2a78e}
.card--red .card__list{background:linear-gradient(#fbe0d6,#fff 90%)}
</style>
</head>
<body>

<!-- Page 1: Right eating habits -->
<section class="page page--eating">
  <header class="page__header">
    <div class="page__kicker">Right Eating and Bowel Habits</div>
    <div class="page__title">FOR BEST HEALTH</div>
  </header>

  <svg class="wheel" width="260" height="260" viewBox="-130 -130 260 260" aria-label="Eating habits wheel">
    <defs>
      <path id="wedge" d="M0,-118 A118,118 0 0 1 63.8,-99.3 L29.7,-46.3 A55,55 0 0 0 0,-55 Z"/>
      <radialGradient id="bowl" cx="50%" cy="45%" r="60%">
        <stop offset="0" stop-color="#f2c35a"/><stop offset=".45" stop-color="#7a5a3a"/><stop offset="1" stop-color="#2f2d2a"/>
      </radialGradient>
    </defs>
    <use href="#wedge" fill="#2d3558"/>
    <use href="#wedge" fill="#1a8fd4" transform="rotate(32.73)"/>
    <use href="#wedge" fill="#1f9a3e" transform="rotate(65.45)"/>
    <use href="#wedge" fill="#5cb84a" transform="rotate(98.18)"/>
    <use href="#wedge" fill="#a26a45" transform="rotate(130.9)"/>
    <use href="#wedge" fill="#d91f26" transform="rotate(163.6)"/>
    <use href="#wedge" fill="#7b7e83" transform="rotate(196.4)"/>
    <use href="#wedge" fill="#f7d417" transform="rotate(229.1)"/>
    <use href="#wedge" fill="#f58220" transform="rotate(261.8)"/>
    <use href="#wedge" fill="#f4ae3e" transform="rotate(294.5)"/>
    <use href="#wedge" fill="#8e4a96" transform="rotate(327.3)"/>
    <circle r="58" fill="#fff" opacity=".35"/>
    <circle r="53" fill="#fff"/>
    <circle r="49" fill="url(#bowl)" role="img" aria-label="Photo of a vegetable rice bowl with egg"/>
  </svg>

  <div class="tip tip--right" style="right:243px;top:121px">Eat <b>Slowly</b>.<br>Chew food well and<br>mix with saliva</div>
  <div class="tip" style="left:238px;top:125px"><b>5 Hours</b> gap<br>between meals is<br>a must</div>
  <div class="tip" style="left:320px;top:172px"><b>Do Not</b> eat in<br>between meals.<br>No snacks.</div>
  <div class="tip" style="left:348px;top:243px">Avoid<br><b>Extreme</b> hot<br>and cold foods</div>
  <div class="tip" style="left:339px;top:317px"><b>Do Not</b> drink<br>water with meals.<br>Drink1/2 an hour<br>before and 1 hour<br>after meals.</div>
  <div class="tip" style="left:288px;top:386px">Avoid <b>Overeating</b>.<br>Eat only what is required.</div>
  <div class="tip tip--center" style="left:150px;width:124px;top:413px"><b>Avoid</b><br>condiments, spices, greasy<br>and fatty foods</div>
  <div class="tip tip--right" style="right:291px;top:384px">After each meal <b>Empty</b><br>the bowel. which contains<br>previous meal's waste</div>
  <div class="tip tip--right" style="right:339px;top:322px"><b>Light</b> Dinner,<br>preferably Fruits</div>
  <div class="tip tip--right" style="right:351px;top:247px"><b>Moderate</b><br>Lunch</div>
  <div class="tip tip--right" style="right:320px;top:178px">Eat <b>Heavy</b><br>Breakfast</div>

  <p class="quote">Those who will not eat and drink from principle,<br>will not be governed by principle in other things.</p>

  <div class="acronym">
    <svg class="acronym__arc" width="80" height="80" viewBox="0 0 80 80"><path d="M34.3,7.5 A33,33 0 0 1 34.3,72.5" fill="none" stroke="#8a8d96" stroke-width="1.4" stroke-dasharray="2 2"/></svg>
    <span class="acronym__item" style="transform:rotate(-82deg) translateX(36px)"><b class="acronym__letter" style="transform:rotate(82deg)">M</b>— RIGHT NUTRITION</span>
    <span class="acronym__item" style="transform:rotate(-73.8deg) translateX(36px)"><b class="acronym__letter" style="transform:rotate(73.8deg)">E</b>— EXERCISE</span>
    <span class="acronym__item" style="transform:rotate(-65.6deg) translateX(36px)"><b class="acronym__letter" style="transform:rotate(65.6deg)">A</b>— SUNLIGHT</span>
    <span class="acronym__item" style="transform:rotate(-57.4deg) translateX(36px)"><b class="acronym__letter" style="transform:rotate(57.4deg)">D</b>— TEMPERANCE</span>
    <span class="acronym__item" style="transform:rotate(-49.2deg) translateX(36px)"><b class="acronym__letter" style="transform:rotate(49.2deg)">O</b>— OPTIMAL WATER INTAKE</span>
    <span class="acronym__item" style="transform:rotate(-41deg) translateX(36px)"><b class="acronym__letter" style="transform:rotate(41deg)">W</b>— REST</span>
    <span class="acronym__item" style="transform:rotate(-32.8deg) translateX(36px)"><b class="acronym__letter" style="transform:rotate(32.8deg)">B</b>— AIR</span>
    <span class="acronym__item" style="transform:rotate(-24.6deg) translateX(36px)"><b class="acronym__letter" style="transform:rotate(24.6deg)">R</b>— TRUST IN DIVINE POWER</span>
    <span class="acronym__item" style="transform:rotate(-16.4deg) translateX(36px)"><b class="acronym__letter" style="transform:rotate(16.4deg)">O</b>— INITIATING SOCIAL SUPPORT</span>
    <span class="acronym__item" style="transform:rotate(-8.2deg) translateX(36px)"><b class="acronym__letter" style="transform:rotate(8.2deg)">O</b>— OPTIMISM</span>
    <span class="acronym__item" style="transform:rotate(0deg) translateX(36px)"><b class="acronym__letter">K</b>— NEW BEGINNING</span>
  </div>
  <div class="brand">MEADOWBROOK<br>HEALTH CARE</div>
  <div class="page__strip"></div>
</section>

<!-- Page 2: Food pyramid -->
<section class="page page--pyramid">
  <header class="page__header"><div class="page__title">Healthy Food Pyramid</div></header>
  <p class="intro">Saeceperro in et accab ipsunt verum quam nobit quunt ulpa alignam faccaborum ipsum derum qui tem dolupti onsecte voluptiis et everumquae volessedit, que et lacit, invenis quibusa ndiatin cores eris el maiosant aut alissunti resequi res doluptio. Empedic aborem faccati busam, se vendell iaecullit qui dolorae num repudam.</p>

  <svg class="pyramid" width="424" height="548" viewBox="0 0 424 548" aria-label="Food pyramid">
    <defs>
      <linearGradient id="strip" x1="0" x2="1">
        <stop offset="0" stop-color="#dcdcdc"/><stop offset=".5" stop-color="#f4f4f4"/><stop offset=".75" stop-color="#e2e2e2"/><stop offset="1" stop-color="#f2f2f2"/>
      </linearGradient>
      <clipPath id="pyr"><polygon points="214,183 84,401 283,429 316,410"/></clipPath>
    </defs>
    <rect x="0" y="199" width="424" height="33" fill="url(#strip)"/>
    <rect x="0" y="233" width="424" height="33" fill="url(#strip)"/>
    <rect x="0" y="268" width="424" height="33" fill="url(#strip)"/>
    <rect x="0" y="302" width="424" height="33" fill="url(#strip)"/>
    <rect x="0" y="336" width="424" height="33" fill="url(#strip)"/>
    <rect x="0" y="370" width="424" height="33" fill="url(#strip)"/>
    <g clip-path="url(#pyr)">
      <rect x="0" y="180" width="424" height="52" fill="#f0b33f"/>
      <rect x="0" y="232" width="424" height="35" fill="#27a84a"/>
      <rect x="0" y="267" width="424" height="35" fill="#c98a52"/>
      <rect x="0" y="302" width="424" height="34" fill="#f4ae3e"/>
      <rect x="0" y="336" width="424" height="33" fill="#f58220"/>
      <rect x="0" y="369" width="424" height="62" fill="#5cb84a"/>
      <polygon points="214,183 283,429 316,410" fill="#fff" opacity=".28"/>
    </g>
    <path d="M282,183 H287 V296 H282 M287,240 h4" fill="none" stroke="#8a8d96" stroke-width=".8"/>
    <path d="M313,338 H318 V412 H313 M318,375 h4" fill="none" stroke="#8a8d96" stroke-width=".8"/>
  </svg>

  <div class="level-label" style="right:258px;top:210px">Cold pressed oils</div>
  <div class="level-label" style="right:274px;top:244px">Medicinal herbs</div>
  <div class="level-label" style="right:291px;top:278px">Nuts and seeds</div>
  <div class="level-label" style="right:308px;top:312px">Legumes and cereals</div>
  <div class="level-label" style="right:325px;top:346px">Fruits and vegetables</div>
  <div class="level-label" style="right:343px;top:380px">Leafy dolendis</div>

  <div class="side-note" style="left:299px;top:230px">velibus accus dolendis<br><b>inienem. Parcitio es</b></div>
  <div class="side-note" style="left:293px;top:306px">Proteins and carbohydrates<br><b>inienem. Parcitio es aut</b></div>
  <div class="side-note" style="left:329px;top:364px">velibus accus dolendis<br><b>inienem. Parcitio es</b></div>

  <div class="acronym">
    <svg class="acronym__arc" width="80" height="80" viewBox="0 0 80 80"><path d="M34.3,7.5 A33,33 0 0 1 34.3,72.5" fill="none" stroke="#8a8d96" stroke-width="1.4" stroke-dasharray="2 2"/></svg>
    <span class="acronym__item" style="transform:rotate(-82deg) translateX(36px)"><b class="acronym__letter" style="transform:rotate(82deg)">M</b>— RIGHT NUTRITION</span>
    <span class="acronym__item" style="transform:rotate(-73.8deg) translateX(36px)"><b class="acronym__letter" style="transform:rotate(73.8deg)">E</b>— EXERCISE</span>
    <span class="acronym__item" style="transform:rotate(-65.6deg) translateX(36px)"><b class="acronym__letter" style="transform:rotate(65.6deg)">A</b>— SUNLIGHT</span>
    <span class="acronym__item" style="transform:rotate(-57.4deg) translateX(36px)"><b class="acronym__letter" style="transform:rotate(57.4deg)">D</b>— TEMPERANCE</span>
    <span class="acronym__item" style="transform:rotate(-49.2deg) translateX(36px)"><b class="acronym__letter" style="transform:rotate(49.2deg)">O</b>— OPTIMAL WATER INTAKE</span>
    <span class="acronym__item" style="transform:rotate(-41deg) translateX(36px)"><b class="acronym__letter" style="transform:rotate(41deg)">W</b>— REST</span>
    <span class="acronym__item" style="transform:rotate(-32.8deg) translateX(36px)"><b class="acronym__letter" style="transform:rotate(32.8deg)">B</b>— AIR</span>
    <span class="acronym__item" style="transform:rotate(-24.6deg) translateX(36px)"><b class="acronym__letter" style="transform:rotate(24.6deg)">R</b>— TRUST IN DIVINE POWER</span>
    <span class="acronym__item" style="transform:rotate(-16.4deg) translateX(36px)"><b class="acronym__letter" style="transform:rotate(16.4deg)">O</b>— INITIATING SOCIAL SUPPORT</span>
    <span class="acronym__item" style="transform:rotate(-8.2deg) translateX(36px)"><b class="acronym__letter" style="transform:rotate(8.2deg)">O</b>— OPTIMISM</span>
    <span class="acronym__item" style="transform:rotate(0deg) translateX(36px)"><b class="acronym__letter">K</b>— NEW BEGINNING</span>
  </div>
  <div class="brand">MEADOWBROOK<br>HEALTH CARE</div>
  <div class="page__strip"></div>
</section>

<!-- Page 3: Food codes -->
<section class="page page--codes">
  <header class="page__header"><div class="page__title">Green, Yellow, and Red<br>Foods codes</div></header>
  <div class="dots"><span style="background:var(--green-bright)"></span><span style="background:var(--yellow)"></span><span style="background:var(--red)"></span></div>
  <div class="photo-band" role="img" aria-label="Photo of chia seeds in a white bowl beside a salad of tomatoes, egg and sweet potato"></div>

  <div class="table">
    <div class="row-key" style="top:306px;background:var(--row-green)"><div class="row-key__dot" style="background:var(--green)">
      <svg width="18" height="14" viewBox="0 0 18 14"><path d="M2,7 L7,12 L16,2" fill="none" stroke="#fff" stroke-width="3" stroke-linecap="round" stroke-linejoin="round"/></svg></div></div>
    <div class="row-key" style="top:351px;background:var(--row-yellow)"><div class="row-key__dot" style="background:var(--yellow)">
      <svg width="18" height="16" viewBox="0 0 18 16"><polygon points="9,1 17,15 1,15" fill="#fff"/></svg></div></div>
    <div class="row-key" style="top:396px;background:var(--row-red)"><div class="row-key__dot" style="background:var(--red)">
      <svg width="18" height="18" viewBox="0 0 18 18"><polygon points="5.5,1 12.5,1 17,5.5 17,12.5 12.5,17 5.5,17 1,12.5 1,5.5" fill="#fff"/></svg></div></div>

    <div class="col" style="left:75px"><div class="col__icon"></div><div class="col__head">PROCESSING</div><div class="col__arrow"></div></div>
    <div class="col" style="left:141px"><div class="col__icon"></div><div class="col__head">NUTRIENTS</div><div class="col__arrow"></div></div>
    <div class="col" style="left:207px"><div class="col__icon"></div><div class="col__head">FIBER</div><div class="col__arrow"></div></div>
    <div class="col" style="left:273px"><div class="col__icon"></div><div class="col__head">SUGAR</div><div class="col__arrow"></div></div>
    <div class="col" style="left:339px"><div class="col__icon"></div><div class="col__head">FAT</div><div class="col__arrow"></div></div>

    <div class="cell" style="left:75px;top:305px;background:var(--row-green)">Least-processed</div>
    <div class="cell" style="left:141px;top:305px;background:var(--row-green)">Whole foods,<br>Nutrient packed</div>
    <div class="cell" style="left:207px;top:305px;background:var(--row-green)">High in fiber</div>
    <div class="cell" style="left:273px;top:305px;background:var(--row-green)">Low in added<br>sugar</div>
    <div class="cell" style="left:339px;top:305px;background:var(--row-green)">Healthy fats</div>

    <div class="cell" style="left:75px;top:350px;background:var(--row-yellow)">Some processing</div>
    <div class="cell" style="left:141px;top:350px;background:var(--row-yellow)">Some healthful<br>Nutrients</div>
    <div class="cell" style="left:207px;top:350px;background:var(--row-yellow)">Lower in fiber</div>
    <div class="cell" style="left:273px;top:350px;background:var(--row-yellow)">Added sugar or<br>Artificial<br>sweetners</div>
    <div class="cell" style="left:339px;top:350px;background:var(--row-yellow)">Poor-quality fats</div>

    <div class="cell" style="left:75px;top:395px;background:var(--row-red)">Most-processed<br>foods</div>
    <div class="cell" style="left:141px;top:395px;background:var(--row-red)">Lowest-quality<br>ingredients</div>
    <div class="cell" style="left:207px;top:395px;background:var(--row-red)">Minimal fiber</div>
    <div class="cell" style="left:273px;top:395px;background:var(--row-red)">Added sugar<br>or artificial<br>sweetners</div>
    <div class="cell" style="left:339px;top:395px;background:var(--row-red)">Excess fats and/<br>or trans fat fried<br>foods</div>
  </div>

  <div class="acronym">
    <svg class="acronym__arc" width="80" height="80" viewBox="0 0 80 80"><path d="M34.3,7.5 A33,33 0 0 1 34.3,72.5" fill="none" stroke="#8a8d96" stroke-width="1.4" stroke-dasharray="2 2"/></svg>
    <span class="acronym__item" style="transform:rotate(-82deg) translateX(36px)"><b class="acronym__letter" style="transform:rotate(82deg)">M</b>— RIGHT NUTRITION</span>
    <span class="acronym__item" style="transform:rotate(-73.8deg) translateX(36px)"><b class="acronym__letter" style="transform:rotate(73.8deg)">E</b>— EXERCISE</span>
    <span class="acronym__item" style="transform:rotate(-65.6deg) translateX(36px)"><b class="acronym__letter" style="transform:rotate(65.6deg)">A</b>— SUNLIGHT</span>
    <span class="acronym__item" style="transform:rotate(-57.4deg) translateX(36px)"><b class="acronym__letter" style="transform:rotate(57.4deg)">D</b>— TEMPERANCE</span>
    <span class="acronym__item" style="transform:rotate(-49.2deg) translateX(36px)"><b class="acronym__letter" style="transform:rotate(49.2deg)">O</b>— OPTIMAL WATER INTAKE</span>
    <span class="acronym__item" style="transform:rotate(-41deg) translateX(36px)"><b class="acronym__letter" style="transform:rotate(41deg)">W</b>— REST</span>
    <span class="acronym__item" style="transform:rotate(-32.8deg) translateX(36px)"><b class="acronym__letter" style="transform:rotate(32.8deg)">B</b>— AIR</span>
    <span class="acronym__item" style="transform:rotate(-24.6deg) translateX(36px)"><b class="acronym__letter" style="transform:rotate(24.6deg)">R</b>— TRUST IN DIVINE POWER</span>
    <span class="acronym__item" style="transform:rotate(-16.4deg) translateX(36px)"><b class="acronym__letter" style="transform:rotate(16.4deg)">O</b>— INITIATING SOCIAL SUPPORT</span>
    <span class="acronym__item" style="transform:rotate(-8.2deg) translateX(36px)"><b class="acronym__letter" style="transform:rotate(8.2deg)">O</b>— OPTIMISM</span>
    <span class="acronym__item" style="transform:rotate(0deg) translateX(36px)"><b class="acronym__letter">K</b>— NEW BEGINNING</span>
  </div>
  <div class="brand">MEADOWBROOK<br>HEALTH CARE</div>
  <div class="page__strip"></div>
</section>

<!-- Page 4: Green / yellow / red foods -->
<section class="page page--restore">
  <header class="page__header"><div class="page__title">Meadowbrook</div></header>

  <article class="card card--green">
    <svg class="card__tab" width="121" height="60" viewBox="0 0 121 60">
      <path d="M0,60 C12,60 31,57 33,44 L33,29 A27.5,27.5 0 0 1 88,29 L88,44 C90,57 109,60 121,60 Z" fill="var(--green)"/>
      <circle cx="60.5" cy="29" r="21" fill="#fff"/><circle cx="60.5" cy="29" r="18" fill="var(--green)"/><circle cx="60.5" cy="29" r="16" fill="#fff"/>
      <path d="M52,29 L58,35 L69,23" fill="none" stroke="var(--green)" stroke-width="3.5" stroke-linecap="round" stroke-linejoin="round"/>
    </svg>
    <div class="card__photo" role="img" aria-label="Photo of colourful fresh fruit and vegetables" style="background:linear-gradient(90deg,#e6a21f,#d9472c 35%,#7fb23a 65%,#3f6d2a)"></div>
    <div class="card__title"><b>Green</b>Light Foods</div>
    <div class="card__lead">Unprocessed whole plant foods naturally low in fat; can be fresh or frozen</div>
    <ul class="card__list" style="height:175px">
      <li><b>Fruits</b> (e.g., bananas, mangoes, oranges)</li>
      <li><b>Starchy vegetables</b> (e.g., potatoes, butternut squash, corn)</li>
      <li><b>Legumes</b> (e.g., beans, lentils, peas)</li>
      <li><b>Intact whole grains</b> (e.g., brown rice, quinoa, farro)</li>
      <li><b>Non-starchy vegetables</b> (e.g., tomatoes, cucumbers, broccoli)</li>
      <li><b>Leafy greens</b> (e.g., lettuce, arugula, spinach)</li>
      <li><b>Herbs and spices</b> (fresh or dried)</li>
      <li><b>Mushrooms</b> (e.g., shiitake, cremini, portobello)</li>
    </ul>
  </article>

  <article class="card card--yellow">
    <svg class="card__tab" width="121" height="60" viewBox="0 0 121 60">
      <path d="M0,60 C12,60 31,57 33,44 L33,29 A27.5,27.5 0 0 1 88,29 L88,44 C90,57 109,60 121,60 Z" fill="var(--yellow)"/>
      <circle cx="60.5" cy="29" r="21" fill="#fff"/><circle cx="60.5" cy="29" r="18" fill="var(--yellow)"/><circle cx="60.5" cy="29" r="16" fill="#fff"/>
      <polygon points="60.5,19 70,36 51,36" fill="var(--yellow)"/>
    </svg>
    <div class="card__photo" role="img" aria-label="Photo of mixed nuts in a bowl" style="background:linear-gradient(90deg,#4a3324,#a9835a 40%,#7a5636 70%,#3a281d)"></div>
    <div class="card__title" style="color:#2a2f45"><b>Yellow</b>Light Foods</div>
    <div class="card__lead">Minimally processed or whole plant foods containing a higher fat content</div>
    <ul class="card__list" style="height:175px">
      <li><b>Avocados</b></li>
      <li><b>Nuts and seeds</b></li>
      <li><b>Nut and seed butters Plant-based milks Coconut meat</b></li>
      <li><b>Soy products</b> (edamame, tofu, tempeh) Olives</li>
      <li><b>Pasta alternatives</b> (e.g., lentil, bean, brown rice) Sprouted bread</li>
      <li><b>Dried fruits</b> (e.g., dates, raisins, dried apricots)</li>
      <li><b>Fermented foods</b> (e.g., sauerkraut, kimchi, coconut kefir)</li>
    </ul>
  </article>

  <article class="card card--red">
    <svg class="card__tab" width="121" height="60" viewBox="0 0 121 60">
      <path d="M0,60 C12,60 31,57 33,44 L33,29 A27.5,27.5 0 0 1 88,29 L88,44 C90,57 109,60 121,60 Z" fill="var(--red)"/>
      <circle cx="60.5" cy="29" r="21" fill="#fff"/><circle cx="60.5" cy="29" r="18" fill="var(--red)"/><circle cx="60.5" cy="29" r="16" fill="#fff"/>
      <polygon points="56.5,19 64.5,19 70.5,25 70.5,33 64.5,39 56.5,39 50.5,33 50.5,25" fill="var(--red)"/>
    </svg>
    <div class="card__photo" role="img" aria-label="Photo of raw red meat cubes on a dark board" style="background:linear-gradient(90deg,#2e3236,#b8484f 35%,#c9606a 60%,#34383c)"></div>
    <div class="card__title"><b>Red</b>Light Foods</div>
    <div class="card__lead">Animal products and highly processed foods</div>
    <ul class="card__list" style="height:175px">
      <li><b>Red meat</b></li>
      <li><b>Whitemeat</b></li>
      <li><b>Eggs</b></li>
      <li><b>All dairy products</b></li>
      <li><b>Oils of any kind</b></li>
      <li><b>Fish and shellfish</b></li>
      <li><b>Processed baked goods</b> (e.g., croissants, muffins, cookies)</li>
      <li><b>Sweeteners</b> (e.g., HFCS, sorbitol, maltodextrin)</li>
      <li><b>Refined "white" foods</b> (e.g., white pasta, white bread, white sugar, white flour)</li>
      <li><b>Coconut products</b> (processed, high-calorie products excluding coconut kefir and aminos, e.g., yogurt, ice cream)</li>
      <li><b>Processed vegan foods</b> (e.g., processed veggie burgers, vegan cheeses, nut milk ice creams)</li>
    </ul>
  </article>

  <div class="acronym">
    <svg class="acronym__arc" width="80" height="80" viewBox="0 0 80 80"><path d="M34.3,7.5 A33,33 0 0 1 34.3,72.5" fill="none" stroke="#8a8d96" stroke-width="1.4" stroke-dasharray="2 2"/></svg>
    <span class="acronym__item" style="transform:rotate(-82deg) translateX(36px)"><b class="acronym__letter" style="transform:rotate(82deg)">M</b>— RIGHT NUTRITION</span>
    <span class="acronym__item" style="transform:rotate(-73.8deg) translateX(36px)"><b class="acronym__letter" style="transform:rotate(73.8deg)">E</b>— EXERCISE</span>
    <span class="acronym__item" style="transform:rotate(-65.6deg) translateX(36px)"><b class="acronym__letter" style="transform:rotate(65.6deg)">A</b>— SUNLIGHT</span>
    <span class="acronym__item" style="transform:rotate(-57.4deg) translateX(36px)"><b class="acronym__letter" style="transform:rotate(57.4deg)">D</b>— TEMPERANCE</span>
    <span class="acronym__item" style="transform:rotate(-49.2deg) translateX(36px)"><b class="acronym__letter" style="transform:rotate(49.2deg)">O</b>— OPTIMAL WATER INTAKE</span>
    <span class="acronym__item" style="transform:rotate(-41deg) translateX(36px)"><b class="acronym__letter" style="transform:rotate(41deg)">W</b>— REST</span>
    <span class="acronym__item" style="transform:rotate(-32.8deg) translateX(36px)"><b class="acronym__letter" style="transform:rotate(32.8deg)">B</b>— AIR</span>
    <span class="acronym__item" style="transform:rotate(-24.6deg) translateX(36px)"><b class="acronym__letter" style="transform:rotate(24.6deg)">R</b>— TRUST IN DIVINE POWER</span>
    <span class="acronym__item" style="transform:rotate(-16.4deg) translateX(36px)"><b class="acronym__letter" style="transform:rotate(16.4deg)">O</b>— INITIATING SOCIAL SUPPORT</span>
    <span class="acronym__item" style="transform:rotate(-8.2deg) translateX(36px)"><b class="acronym__letter" style="transform:rotate(8.2deg)">O</b>— OPTIMISM</span>
    <span class="acronym__item" style="transform:rotate(0deg) translateX(36px)"><b class="acronym__letter">K</b>— NEW BEGINNING</span>
  </div>
  <div class="brand">MEADOWBROOK<br>HEALTH CARE</div>
  <div class="page__strip"></div>
</section>

</body>
</html>
```